Business cards / Letterheads / Compliment slips

We are looking to get business cards, letterheads and compliment slips designed.

These will all have to follow the design of our new website and logo. Links to the website, logo and fonts can be found below...

The designs need to be simple with focus on the typography. Only the following colours should be used on the designs...

#7f9d3c
#191818
#fff

Website:
http://brightfieldweb.samplework.co.uk/

Logo:
https://www.filecrate.example/sh/9xk2mwq7tvbalp4/qrtuPL8NzK/logos

Fonts:
https://www.filecrate.example/sh/9xk2mwq7tvbalp4/Hw7ZpRt3sQ/Fonts/BayerModern_TTF

and

https://www.filecrate.example/sh/9xk2mwq7tvbalp4/T6nVyo4Dc1/Fonts/MuseoSansFamily

Reason: We would like some more design submissions

Reason: We are still deciding on designs we like and would like to see some more submissions...

Industry/Entity Type

Business

Requirements
Must have
• The designs need to be simple with focus on the typography. Only the following colours should be used on the designs...

#7f9d3c
#191818
#fff
Should not have
• - Any fonts that are not provided.
- Any colours that are not provided.

```html
<!DOCTYPE html>
<html lang="en">
<head>
<meta charset="utf-8">
<title>Brightfield Stationery</title>
<link rel="stylesheet" href="https://fonts.googleapis.com/css2?family=Nunito+Sans:wght@300;400;700;800&display=swap">
<style>
:root{
  --green:#7f9d3c;
  --charcoal:#3c3c3b;
  --ink:#191818;
  --white:#fff;
  --backdrop:#e4e4e2;
  --muted:#8a8a88;
}
*{box-sizing:border-box;margin:0;padding:0}
html,body{width:1200px;height:800px;overflow:hidden}
body{background:var(--backdrop);font-family:"Nunito Sans",Arial,sans-serif;color:var(--ink);position:relative}
.sheet{position:absolute;background:var(--white);box-shadow:0 4px 14px rgba(0,0,0,.18)}
.brand{display:flex;align-items:center;gap:6px;font-weight:800;letter-spacing:-.3px;color:var(--white);white-space:nowrap}
.brand .dot{width:14px;height:14px;border-radius:50%;background:var(--green)}
.brand.dark{color:var(--ink)}
.tagline{color:var(--green);font-size:8px;font-weight:400;white-space:nowrap}
.contact{display:flex;gap:16px;align-items:center;font-size:9px;color:var(--white)}
.contact span{display:flex;align-items:center;gap:4px;white-space:nowrap}
.contact i{width:7px;height:7px;border-radius:50%;background:var(--green);display:inline-block;flex:none}

/* letterhead */
.letterhead{left:70px;top:100px;width:420px;height:594px;display:flex;flex-direction:column}
.letterhead .head{height:50px;background:var(--charcoal);display:flex;justify-content:space-between;align-items:flex-end;padding:0 18px 10px}
.letterhead .head .brand{font-size:17px}
.letterhead .head .tagline{align-self:flex-start;margin-top:10px}
.letterhead .body{flex:1}
.letterhead .foot{height:38px;background:var(--charcoal);display:flex;align-items:center;justify-content:center;padding:0 12px;overflow:hidden}
.letterhead .foot .contact{font-size:7px;gap:9px}
.letterhead .foot .contact span{gap:3px}
.letterhead .foot .contact i{width:5px;height:5px}

/* compliment slip */
.slip{left:530px;top:80px;width:600px;height:283px;display:flex;flex-direction:column}
.slip .head{height:62px;background:var(--charcoal);display:flex;justify-content:space-between;align-items:flex-end;padding:0 20px 12px}
.slip .head .brand{font-size:20px}
.slip .head .tagline{align-self:flex-start;margin-top:12px}
.slip .body{flex:1;display:flex;flex-direction:column;align-items:flex-end;padding:22px 20px}
.slip h2{color:var(--green);font-size:22px;font-weight:700}
.slip .contact{color:var(--charcoal);margin-top:8px}

/* business cards */
.card{width:290px;height:170px;top:420px}
.card-back{left:530px;background:var(--charcoal);display:flex;align-items:center;justify-content:center}
.card-back .brand{font-size:24px}
.card-front{left:840px;display:flex;flex-direction:column}
.card-front .main{flex:1;display:flex;justify-content:space-between;padding:22px 16px 10px}
.card-front .brand{font-size:17px;align-self:flex-end}
.card-front .details{text-align:right}
.card-front .name{font-size:14px;font-weight:700}
.card-front .role{font-size:8px;color:var(--muted);margin-bottom:8px}
.card-front .line{font-size:8px;line-height:1.6;display:flex;justify-content:flex-end;align-items:center;gap:4px;white-space:nowrap}
.card-front .line i{width:5px;height:5px;border-radius:50%;background:var(--green)}
.card-front .strip{height:20px;background:var(--charcoal);border-top:3px solid var(--green);display:flex;align-items:center;justify-content:center}
.card-front .strip .tagline{font-size:7px}
</style>
</head>
<body>

<section class="sheet letterhead">
  <header class="head">
    <div class="brand"><span class="dot"></span>brightfield</div>
    <p class="tagline">We fuel search engine marketing for higher profits</p>
  </header>
  <div class="body"></div>
  <footer class="foot">
    <div class="contact">
      <span><i></i>P O Box 5678, Mill Row AU</span>
      <span><i></i>+ 123.555.0142</span>
      <span><i></i>hello@brightfieldweb.com</span>
      <span><i></i>www.brightfieldweb.com</span>
    </div>
  </footer>
</section>

<section class="sheet slip">
  <header class="head">
    <div class="brand"><span class="dot"></span>brightfield</div>
    <p class="tagline">We fuel search engine marketing for higher profits</p>
  </header>
  <div class="body">
    <h2>With Compliments</h2>
    <div class="contact">
      <span><i></i>+ 123.555.0142</span>
      <span><i></i>hello@brightfieldweb.com</span>
      <span><i></i>www.brightfieldweb.com</span>
    </div>
  </div>
</section>

<section class="sheet card card-back">
  <div class="brand"><span class="dot"></span>brightfield</div>
</section>

<section class="sheet card card-front">
  <div class="main">
    <div class="brand dark"><span class="dot"></span>brightfield</div>
    <div class="details">
      <p class="name">Alan Ward</p>
      <p class="role">Account Manager</p>
      <p class="line">P O Box 5678, Mill Row AU <i></i></p>
      <p class="line">+ 123.555.0142 <i></i></p>
      <p class="line">hello@brightfieldweb.com <i></i></p>
      <p class="line">www.brightfieldweb.com <i></i></p>
    </div>
  </div>
  <div class="strip"><p class="tagline">Search marketing that grows your business</p></div>
</section>

</body>
</html>
```